IT Business Card Design

My company is a newly started small IT repair business. I operate outside of usual hours except for Saturday.
I am a very experienced and professional Technician.
I would like the business card to express that I am running a professional business and not some home IT business. This should be expressed through the design of the business card.
On the back of the card I would like the name of the company to be displayed.
Updates
Sorry guys, I have updated the requirement to be double sided. Fantastic submissions so far! Keep up the good work.
Hey designers!
Hey Designers!
Thank you all for your hard work!
Target Market(s)
Home to small business users.
Industry/Entity Type
Business
Contact Information for Business Card
Harbourlight Technics
Marcus Pendleby (Director)
marcus.pendleby@quorvanet.com.au
Operating Hours
5pm-12am Mon - Fri
9am - 5pm Sat
Mobile
0417962351
Requirements
Must have
- The base colour must be matte black. There must be some dark purple. (To go with the "Harbourlight" theme)

```html
<!DOCTYPE html>
<html lang="en">
<head>
<meta charset="utf-8">
<title>Harbourlight Technics – Business Card</title>
<link rel="stylesheet" href="https://fonts.googleapis.com/css2?family=Josefin+Sans:wght@600;700&family=Open+Sans:wght@400&display=swap">
<style>
  :root {
    --backdrop: #2a2a2d;
    --navy: #2e3450;
    --pink: #c2497f;
    --band-pink: #c8407f;
    --band-plum: #7a3c68;
    --plum-light: #8d426f;
    --plum-dark: #66284f;
    --divider: #d8d8d8;
    --title-grey: #dedede;
    --text-white: #f2f2f2;
  }
  * { box-sizing: border-box; }
  html, body {
    margin: 0;
    width: 1200px;
    height: 1200px;
    overflow: hidden;
    background: var(--backdrop);
  }
  .canvas {
    position: relative;
    width: 1200px;
    height: 1200px;
  }
  .card {
    position: absolute;
    left: 110px;
    width: 980px;
    height: 560px;
    overflow: hidden;
    background: var(--navy);
  }
  .card--back { top: 30px; }
  .card--front { top: 610px; }
  .card-shapes {
    position: absolute;
    inset: 0;
    width: 100%;
    height: 100%;
  }
  .brand-title {
    position: absolute;
    left: 70px;
    top: 78px;
    margin: 0;
    font-family: "Josefin Sans", sans-serif;
    font-weight: 700;
    font-size: 102px;
    line-height: 1.08;
    letter-spacing: 2px;
    text-transform: uppercase;
    color: var(--title-grey);
  }
  .card-details {
    position: absolute;
    right: 40px;
    top: 340px;
    text-align: right;
  }
  .card-name {
    margin: 0 0 10px;
    font-family: "Josefin Sans", sans-serif;
    font-weight: 600;
    font-size: 32px;
    letter-spacing: 1.5px;
    text-transform: uppercase;
    color: var(--title-grey);
  }
  .contact-list {
    margin: 0;
    padding: 0;
    list-style: none;
    font-family: "Open Sans", sans-serif;
    font-size: 22px;
    line-height: 28px;
    color: var(--text-white);
  }
  .contact-label { color: var(--pink); }
</style>
</head>
<body>
<main class="canvas">

  <section class="card card--back" aria-label="Card back">
    <svg class="card-shapes" viewBox="0 0 980 560" preserveAspectRatio="none" aria-hidden="true">
      <polygon class="band band--plum" points="0,380 980,250 980,285 0,415" fill="var(--band-plum)"/>
      <polygon class="band band--pink" points="0,440 980,310 980,348 0,478" fill="var(--band-pink)"/>
    </svg>
    <h1 class="brand-title">Harbourlight<br>Technics</h1>
  </section>

  <section class="card card--front" aria-label="Card front">
    <svg class="card-shapes" viewBox="0 0 980 560" preserveAspectRatio="none" aria-hidden="true">
      <defs>
        <linearGradient id="plum-panel" x1="0" y1="0" x2="1" y2="0">
          <stop offset="0" stop-color="var(--plum-light)"/>
          <stop offset="1" stop-color="var(--plum-dark)"/>
        </linearGradient>
      </defs>
      <polygon class="panel panel--pink" points="0,0 490,0 540,240 300,560 0,560" fill="var(--pink)"/>
      <polygon class="panel panel--plum" points="490,0 980,0 980,340 540,240" fill="url(#plum-panel)"/>
      <polygon class="panel panel--navy" points="540,240 980,340 980,560 300,560" fill="var(--navy)"/>
      <g class="dividers" stroke="var(--divider)" stroke-width="8" fill="none">
        <line x1="490" y1="0" x2="540" y2="240"/>
        <line x1="540" y1="240" x2="980" y2="340"/>
        <line x1="540" y1="240" x2="300" y2="560"/>
      </g>
    </svg>
    <div class="card-details">
      <h2 class="card-name">Harbourlight Technics</h2>
      <ul class="contact-list">
        <li><span class="contact-label">director:</span> marcus pendleby</li>
        <li><span class="contact-label">e-mail:</span> marcus.pendleby@quorvanet.com.au</li>
        <li><span class="contact-label">phone:</span> 0417962351</li>
        <li><span class="contact-label">operating hours:</span> 5pm-12am</li>
        <li>Mon - Fri 9am - 5pm</li>
      </ul>
    </div>
  </section>

</main>
</body>
</html>
```